Lesson Lantern

LessonLantern.net will be a place for people looking for information, resources, and advisement to start or continue their education. We want a friendly, inviting site design that makes finding what potential students are looking for simple and easy to navigate. We are not committed to the colors of the logo, so variations on the color scheme are welcome.

Text instructions based on the wireframe: For the site's homepage we'd like a banner at the very top for our Logo and white space to the right of it. See attachments for logo + wireframe. Below that would be navigation. Below that split into 2/3 on the left we would have home page content, and 1/3 on the right we would have the lead form. At the bottom of the page we would have a space for types of degrees, then a footer with copyright info + site info.

See wireframes for additional page layouts.

Industry/Entity Type

Education

Requirements
Must have
• At minimum we are looking for three pages: homepage, choose your degree path page, and content page.
Nice to have
• -White space is appreciated
-Variations on the color scheme are welcome, we are not married to the existing logo's color scheme.

```html
<!DOCTYPE html>
<html lang="en">
<head>
<meta charset="utf-8">
<title>Lesson Lantern</title>
<link href="https://fonts.googleapis.com/css2?family=Open+Sans:wght@400;600;700&family=Archivo+Narrow:wght@700&family=Cabin:wght@400;600&family=Kaushan+Script&family=Arimo&display=swap" rel="stylesheet">
<style>
:root{
  --page-blue:#2c4a5d;
  --page-deep:#1e3442;
  --band-dark:#1c2b34;
  --orange:#e8742a;
  --gold:#f0c85a;
  --ink:#1d4258;
  --text-light:#ffffff;
  --label-blue:#2a5e80;
  --field-border:#9aaab5;
  --header-bg:#f4f4f4;
}
*{margin:0;padding:0;box-sizing:border-box}
html,body{width:1200px;height:938px;overflow:hidden}
body{position:relative;font-family:"Open Sans",sans-serif;
  background:radial-gradient(ellipse 60% 45% at 50% 28%,#4d7690 0%,var(--page-blue) 45%,var(--page-deep) 100%);}
.abs{position:absolute}
.site-header{left:0;top:0;width:1200px;height:58px;background:linear-gradient(#fff,var(--header-bg));border-bottom:4px solid var(--orange)}
.brand{left:290px;top:20px;font-family:"Open Sans",sans-serif;font-weight:600;font-size:22px;color:var(--ink);display:flex;align-items:center;gap:8px}
.brand-dot{width:12px;height:12px;background:var(--orange)}
.contact{right:288px;top:8px;text-align:right;font-family:"Arimo",sans-serif;font-size:11px;color:#222;line-height:12px}
.contact .phone-icon{position:absolute;left:-26px;top:1px}
.contact .address{color:var(--orange);font-size:7px;margin-top:2px}
.main-nav{left:288px;top:80px;width:624px;height:25px;background:linear-gradient(#3a5566,#2a4150);border-top:1px solid #6a8494;border-bottom:1px solid #6a8494;font-size:10px;color:#fff}
.main-nav a{position:absolute;top:0;color:#fff;text-decoration:none;line-height:24px;white-space:nowrap}
.main-nav a.current{background:linear-gradient(#fff,#dfe3e6);color:#111;font-weight:600;width:70px;text-align:center}
.main-nav a.bucket{color:var(--gold);font-weight:700;display:flex;align-items:center;gap:6px}
.hero{left:288px;top:120px;width:625px;height:187px;overflow:hidden;background:#f0ede8}
.hero-photo{left:190px;top:0;width:435px;height:187px;background:linear-gradient(100deg,#f2ece4 0%,#d9a98a 25%,#c99170 45%,#3f8fc7 60%,#2c73a8 80%,#7a4a34 100%);clip-path:polygon(0 0,100% 0,100% 100%,70px 100%)}
.hero h1{left:10px;top:14px;width:170px;font-family:"Archivo Narrow",sans-serif;font-size:19px;line-height:22.5px;color:var(--ink)}
.hero p{left:11px;top:90px;width:205px;font-size:9.4px;line-height:13.5px;color:#222}
.dots{right:11px;top:167px;display:flex;gap:3px}
.dots span{width:11px;height:11px;border-radius:50%;background:#ddd;border:1px solid #999}
.dots span.on{background:var(--orange)}
.arrow{top:192px;width:32px;height:32px}
.dropdown{left:777px;top:113px;width:126px;height:128px;background:rgba(40,60,72,.96);border:1px solid #6f8795;font-size:10px;color:#fff;padding-top:4px}
.dropdown div{padding:0 8px;line-height:20px;white-space:nowrap}
.dropdown div.active{background:#1a2a33;color:var(--gold)}
.content{left:290px;top:342px;width:375px;font-size:7.6px;line-height:10.4px;color:var(--text-light)}
.content p{margin-bottom:10.4px}
.form-title{left:712px;top:335px;font-family:"Kaushan Script",cursive;font-size:27px;line-height:25px;color:#fff;transform:rotate(-4deg)}
.form-title span{display:block;padding-left:30px}
.lead-form{left:685px;top:405px;width:226px;height:293px;background:#fff;border-radius:4px;box-shadow:0 0 6px rgba(0,0,0,.4)}
.lead-form .intro{left:7px;top:5px;width:214px;font-size:6.8px;font-weight:700;line-height:9.5px;color:#111}
.req{left:99px;top:40px;font-size:5.6px;font-weight:700;color:#222}
.req b,.row label b{color:#d22}
.row{left:8px;width:214px;height:16px;display:flex;align-items:center}
.row label{width:92px;font-size:7.6px;font-weight:700;color:var(--label-blue);white-space:nowrap}
.field{height:16px;border:1px solid var(--field-border);border-radius:2px;font-size:6.3px;color:#333;padding-left:4px;line-height:14px;background:#fff;position:relative;white-space:nowrap;overflow:hidden}
.select .caret{position:absolute;right:0;top:0;width:16px;height:14px;background:linear-gradient(#5d8fb3,#2e5f85)}
.request-btn{left:9px;top:258px;width:208px;height:27px;background:linear-gradient(#3b4650,#1f272d);border-radius:4px;color:#fff;font-weight:700;font-size:12.5px;display:flex;align-items:center;gap:14px;padding-left:12px;white-space:nowrap}
.degrees{left:0;top:728px;width:1200px;height:144px;background:var(--band-dark);border-bottom:4px solid #6f9ab5}
.degree{top:14px;width:200px}
.degree h2{font-family:"Cabin",sans-serif;font-weight:400;font-size:14.5px;color:var(--gold);margin-bottom:6px;white-space:nowrap}
.degree p{font-size:6.5px;line-height:9px;color:#fff;white-space:nowrap}
.degree a{display:block;margin-top:9px;font-size:6.7px;color:var(--gold);text-decoration:none}
.divider{top:20px;width:1px;height:110px;background:linear-gradient(transparent,#5c6b74,transparent)}
.site-footer{left:0;top:876px;width:1200px;height:62px;background:#f3f3f3;text-align:center;font-family:"Arimo",sans-serif;font-size:8.4px;color:#222;padding-top:23px}
</style>
</head>
<body>
<header class="site-header abs">
  <div class="brand abs"><span class="brand-dot"></span>Lesson Lantern</div>
  <div class="contact abs">
    <svg class="phone-icon" width="20" height="20" viewBox="0 0 20 20"><rect width="20" height="20" rx="4" fill="#e8742a"/><path d="M6 4c1 0 2 2 2 3s-1 1-1 2 2 3 3 3 1-1 2-1 3 1 3 2-1 3-3 3C8 16 4 12 4 7c0-2 1-3 2-3z" fill="#fff"/></svg>
    Telephone: 555-014-2200<br>Facsimile:&nbsp; 555-014-2201
    <div class="address">742 Orchard Lane, Fairview, CA 90210</div>
  </div>
</header>

<nav class="main-nav abs">
  <a class="current" href="#" style="left:37px">Home</a>
  <a href="#" style="left:116px">About Us</a>
  <a href="#" style="left:184px">Contact Us</a>
  <a href="#" style="left:259px">Privacy Policy</a>
  <a href="#" style="left:346px">Terms of use</a>
  <a href="#" style="left:430px">Feedback</a>
  <a class="bucket" href="#" style="left:496px">Choose your bucket <svg width="9" height="7" viewBox="0 0 9 7"><path d="M1 1l3.5 4L8 1" stroke="#f0c85a" stroke-width="2" fill="none"/></svg></a>
</nav>

<section class="hero abs">
  <div class="hero-photo abs" role="img" aria-label="Photo of two smiling students together"></div>
  <h1 class="abs">Take control of your future by furthering your education.</h1>
  <p class="abs">Are you overwhelmed by the thought of choosing the right college? Lesson Lantern helps simplify this process by matching colleges to you and your needs. Tell us about yourself and let us do the work for you.</p>
  <div class="dots abs"><span></span><span></span><span class="on"></span></div>
</section>
<svg class="arrow abs" style="left:267px" viewBox="0 0 32 32"><circle cx="16" cy="16" r="15" fill="#e8742a" stroke="#fff" stroke-width="2"/><path d="M19 8l-8 8 8 8" stroke="#fff" stroke-width="3" fill="none"/></svg>
<svg class="arrow abs" style="left:899px" viewBox="0 0 32 32"><circle cx="16" cy="16" r="15" fill="#e8742a" stroke="#fff" stroke-width="2"/><path d="M13 8l8 8-8 8" stroke="#fff" stroke-width="3" fill="none"/></svg>

<div class="dropdown abs">
  <div>Lorem ipsum dolor sit</div><div>Amet consectetur</div><div class="active">Adipiscing elit</div><div>Lorem ipsum dolor sit</div><div>Amet consectetur</div><div>Adipiscing elit.</div>
</div>

<main class="content abs">
  <p>Lorem ipsum dolor sit amet, consectetur adipiscing elit. Cras vestibulum facilisis malesuada. Morbi mollis neque vel turpis condimentum eu varius ligula ultrices. Aenean lorem nulla, pretium id molestie a, accumsan vel ipsum. Quisque vulputate, lacus at hendrerit sagittis, augue nunc convallis lorem, et aliquet erat nunc quis mauris. Nunc dictum egestas iaculis. Quisque egestas odio non justo ornare quis sagittis turpis molestie. Pellentesque luctus vulputate semper. Etiam adipiscing augue lorem, in luctus lacus. Aliquam erat volutpat.</p>
  <p>Nullam non est sit amet erat vehicula elementum placerat vel urna. Suspendisse eleifend tincidunt fermentum. Sed convallis, augue vitae pretium adipiscing, quam mauris malesuada quam, at consectetur elit dolor vitae ipsum. Quisque eget nisl ac sem molestie dictum. Donec eget enim tellus, a porttitor erat. Curabitur vitae urna sed nunc lacinia dignissim ac et felis. Nulla porttitor dolor at mi bibendum placerat. Sed dapibus adipiscing sem, sed lacinia orci facilisis eleifend.</p>
  <p>Cras a erat leo. Duis pulvinar pharetra nisi ut pharetra. Duis fermentum tellus posuere velit vehicula a bibendum arcu interdum. Fusce placerat nunc eu ligula sagittis at varius ante faucibus. Proin mi ante, dictum at eleifend vitae, porta sit amet tortor. Donec tristique nibh id sapien elementum in auctor sapien eleifend. Sed gravida, urna at dignissim lacinia, metus elit dignissim enim, a eleifend enim massa aliquet est. Nunc a neque tellus, eu porta elit. Cras vitae libero velit. Fusce quis nisi augue, vitae porttitor justo. Nulla turpis tortor, volutpat vel dictum vitae, molestie eget ligula. Vestibulum elementum justo vel odio consectetur faucibus. Morbi ac consectetur mi. Curabitur metus erat, ultricies vel volutpat dapibus, dictum et purus. Curabitur vitae felis massa, sit amet imperdiet lectus.</p>
  <p>Praesent massa mauris, dictum eu eleifend luctus, aliquet at ipsum. Nullam massa nibh, pulvinar condimentum pellentesque ac, feugiat sit amet tellus. Donec ut lectus tortor, eu hendrerit nibh. Quisque blandit, odio in consequat consequat, nisi lectus fermentum nisi, in consectetur tellus est sed diam. Suspendisse vestibulum fringilla mollis. Nam id mollis dui. Nam ligula dolor, sollicitudin in feugiat nec, faucibus convallis elit. Aliquam porttitor ligula iaculis sem pharetra vestibulum at sed eros. Maecenas facilisis mi ut massa suscipit venenatis ut eget nunc. Aliquam at libero eget nulla pharetra gravida et at risus. Proin eget nibh eget leo pellentesque tempus. Morbi consequat luctus tristique.</p>
  <p>Pellentesque felis ligula, mollis in vestibulum ac, pretium sodales nibh. Integer eleifend erat velit. Sed magna ligula, gravida sit amet tincidunt quis, volutpat in enim. Donec lorem tellus, sollicitudin vel vestibulum non, dapibus iaculis enim. Phasellus condimentum metus ultricies leo fermentum nec tincidunt nisi eleifend. Quisque mattis, arcu id vehicula venenatis, quam ipsum tempus elit, at eleifend.</p>
</main>

<div class="form-title abs">Tell us more<span>about YOU!</span></div>

<form class="lead-form abs">
  <p class="intro abs">Lesson Lantern provides you with accredited school information that match your interests. Get matched tothe right schools today.</p>
  <div class="req abs"><b>*</b> Required fields</div>
  <div class="row abs" style="top:52px"><label>Subject <b>*</b></label><div class="field select" style="width:118px">Choose One<span class="caret"></span></div></div>
  <div class="row abs" style="top:74px"><label>Degree Level <b>*</b></label><div class="field select" style="width:118px">Choose One<span class="caret"></span></div></div>
  <div class="row abs" style="top:96px"><label>High School Grad Yr. <b>*</b></label><div class="field select" style="width:118px">Choose One<span class="caret"></span></div></div>
  <div class="row abs" style="top:118px"><label>First Name <b>*</b></label><div class="field" style="width:118px"></div></div>
  <div class="row abs" style="top:140px"><label>Last Name <b>*</b></label><div class="field" style="width:118px"></div></div>
  <div class="row abs" style="top:162px"><label>Street Adress <b>*</b></label><div class="field" style="width:118px"></div></div>
  <div class="row abs" style="top:184px"><label>Zip / City / State <b>*</b></label><div class="field" style="width:31px"></div><div class="field" style="width:54px;margin-left:2px">Enter Your City</div><div class="field" style="width:31px;margin-left:2px">State</div></div>
  <div class="row abs" style="top:206px"><label>Phone Number <b>*</b></label><div class="field" style="width:118px">(&nbsp;&nbsp;&nbsp;&nbsp;)</div></div>
  <div class="row abs" style="top:228px"><label>Email Adress <b>*</b></label><div class="field" style="width:118px"></div></div>
  <div class="request-btn abs">
    <svg width="14" height="16" viewBox="0 0 14 16"><path d="M3 7V5a4 4 0 018 0v2" stroke="#f0c85a" stroke-width="2" fill="none"/><rect x="1" y="7" width="12" height="9" rx="1" fill="#f0c85a"/></svg>
    REQUEST INFORMATION
  </div>
</form>

<section class="degrees abs">
  <div class="degree abs" style="left:298px"><h2>Graduate Degrees</h2><p>Lorem ipsum dolor sit amet, consectetur adipiscing elit.<br>Cras vestibulum facilisis malesuada. Morbi mollis<br>neque vel turpis condimentum eu varius ligula ultrices.<br>Aenean lorem nulla, pretium id molestie a,<br>accumsan vel ipsum. Quisque vulputate, lacus at hendrerit<br>sagittis, augue nunc convallis lorem, et aliquet.<br>erat nunc quis mauris. Nunc dictum egestas iaculis. Quisque<br>egestas odio non justo ornare quis sagittis turpis molestie.</p><a href="#">Learn more &gt;</a></div>
  <div class="divider abs" style="left:495px"></div>
  <div class="degree abs" style="left:508px"><h2>Master's Degrees</h2><p>Lorem ipsum dolor sit amet, consectetur adipiscing elit.<br>Cras vestibulum facilisis malesuada. Morbi mollis<br>neque vel turpis condimentum eu varius ligula ultrices.<br>Aenean lorem nulla, pretium id molestie a,<br>accumsan vel ipsum. Quisque vulputate, lacus at hendrerit<br>sagittis, augue nunc convallis lorem, et aliquet.<br>erat nunc quis mauris. Nunc dictum egestas iaculis. Quisque<br>egestas odio non justo ornare quis sagittis turpis molestie.</p><a href="#">Learn more &gt;</a></div>
  <div class="divider abs" style="left:703px"></div>
  <div class="degree abs" style="left:720px"><h2>Doctoral Degrees</h2><p>Lorem ipsum dolor sit amet, consectetur adipiscing elit.<br>Cras vestibulum facilisis malesuada. Morbi mollis<br>neque vel turpis condimentum eu varius ligula ultrices.<br>Aenean lorem nulla, pretium id molestie a,<br>accumsan vel ipsum. Quisque vulputate, lacus at hendrerit<br>sagittis, augue nunc convallis lorem, et aliquet.<br>erat nunc quis mauris. Nunc dictum egestas iaculis. Quisque<br>egestas odio non justo ornare quis sagittis turpis molestie.</p><a href="#">Learn more &gt;</a></div>
</section>

<footer class="site-footer abs">Copyright 2009-2012 LessonLantern.net™ &amp; Northgate Learning, Inc. All Rights Reserved.</footer>
</body>
</html>
```